Quarlwick Builders Business Cards

I want to use the logo and make an unique business card that shows the textured Logo with brick and builings. I want to be able to stand out when I pass out business cards.

```html
<!DOCTYPE html>
<html lang="en">
<head>
<meta charset="utf-8">
<title>Quarlwick Builders Business Cards</title>
<link rel="stylesheet" href="https://fonts.googleapis.com/css2?family=Montserrat:wght@500;600;700;800&family=Anton&display=swap">
<style>
  :root {
    --page-bg: #2f2f31;
    --card-white: #ffffff;
    --brand-orange: #e2532a;
    --ink: #1b1b1b;
    --band-black: #0d0d0d;
    --concrete-light: #a4a4a4;
    --concrete-mid: #8c8c8c;
    --concrete-dark: #6f6f6f;
    --services-ink: #1f1f1f;
  }
  * { box-sizing: border-box; margin: 0; padding: 0; }
  html, body { width: 1200px; height: 1200px; overflow: hidden; }
  body {
    background: var(--page-bg);
    font-family: "Montserrat", sans-serif;
    position: relative;
  }
  .card {
    position: absolute;
    left: 150px;
    width: 900px;
    height: 514px;
    border-radius: 36px;
    overflow: hidden;
    box-shadow: 0 14px 30px rgba(0,0,0,0.45);
  }
  /* Front */
  .card-front { top: 62px; background: var(--card-white); }
  .front-contact {
    position: absolute;
    left: 64px;
    top: 150px;
  }
  .person-name {
    font-size: 60px;
    font-weight: 700;
    color: var(--brand-orange);
    line-height: 1;
    letter-spacing: 0.5px;
  }
  .person-title {
    font-size: 32px;
    font-weight: 500;
    color: var(--ink);
    line-height: 1.2;
    margin-top: 6px;
    margin-bottom: 14px;
    letter-spacing: 1px;
  }
  .contact-list { list-style: none; }
  .contact-list li {
    display: flex;
    align-items: flex-start;
    gap: 14px;
    font-size: 25px;
    font-weight: 500;
    color: var(--ink);
    line-height: 1.16;
    margin-bottom: 5px;
  }
  .contact-list svg { width: 24px; height: 24px; flex: none; margin-top: 3px; fill: var(--brand-orange); }
  .front-brand {
    position: absolute;
    right: 70px;
    top: 120px;
    width: 340px;
    display: flex;
    align-items: center;
    gap: 16px;
  }
  .brand-square {
    width: 42px;
    height: 42px;
    background: var(--brand-orange);
    flex: none;
  }
  .brand-name {
    font-family: "Montserrat", sans-serif;
    font-weight: 800;
    font-size: 40px;
    line-height: 1.05;
    color: var(--brand-orange);
    text-transform: uppercase;
  }
  .front-band {
    position: absolute;
    left: 0; right: 0; bottom: 0;
    height: 30px;
    display: flex;
  }
  .band-orange { width: 64%; background: var(--brand-orange); }
  .band-gap { width: 14px; background: var(--card-white); }
  .band-black { flex: 1; background: var(--band-black); }
  /* Back */
  .card-back { top: 626px; }
  .concrete-surface {
    position: absolute; inset: 0;
    background:
      radial-gradient(ellipse at 30% 25%, rgba(255,255,255,0.18), transparent 60%),
      radial-gradient(ellipse at 75% 80%, rgba(0,0,0,0.18), transparent 55%),
      linear-gradient(135deg, var(--concrete-light), var(--concrete-mid) 55%, var(--concrete-dark));
  }
  .back-brand {
    position: absolute;
    left: 0; right: 0; top: 170px;
    display: flex;
    justify-content: center;
    align-items: center;
    gap: 22px;
  }
  .back-brand .brand-square { width: 60px; height: 60px; }
  .back-brand .brand-name { font-size: 60px; }
  .services-line {
    position: absolute;
    left: 0; right: 0; bottom: 70px;
    text-align: center;
    font-family: "Anton", sans-serif;
    font-size: 30px;
    letter-spacing: 0.5px;
    color: var(--services-ink);
  }
</style>
</head>
<body>

<section class="card card-front">
  <div class="front-brand">
    <span class="brand-square"></span>
    <span class="brand-name">Quarlwick Builders</span>
  </div>

  <div class="front-contact">
    <h1 class="person-name">FULL NAME</h1>
    <p class="person-title">TITLE</p>
    <ul class="contact-list">
      <li>
        <svg viewBox="0 0 24 24" aria-hidden="true"><path d="M6.6 10.8a15.1 15.1 0 0 0 6.6 6.6l2.2-2.2a1 1 0 0 1 1-.25 11.4 11.4 0 0 0 3.6.57 1 1 0 0 1 1 1V20a1 1 0 0 1-1 1A17 17 0 0 1 3 4a1 1 0 0 1 1-1h3.5a1 1 0 0 1 1 1c0 1.25.2 2.45.57 3.57a1 1 0 0 1-.25 1z"/></svg>
        <span>(000) 000 0000</span>
      </li>
      <li>
        <svg viewBox="0 0 24 24" aria-hidden="true"><path d="M2 5h20v14H2zm2 2v.3l8 5.2 8-5.2V7zm0 2.7V17h16V9.7l-8 5.2z"/></svg>
        <span>email@company.com</span>
      </li>
      <li>
        <svg viewBox="0 0 24 24" aria-hidden="true"><path d="M12 2a10 10 0 1 0 0 20 10 10 0 0 0 0-20zm6.9 9h-3a15 15 0 0 0-1.3-5.6A8 8 0 0 1 18.9 11zM12 4.1c.9 1.2 1.8 3.6 1.9 6.9h-3.8c.1-3.3 1-5.7 1.9-6.9zM9.4 5.4A15 15 0 0 0 8.1 11h-3a8 8 0 0 1 4.3-5.6zM5.1 13h3a15 15 0 0 0 1.3 5.6A8 8 0 0 1 5.1 13zm6.9 6.9c-.9-1.2-1.8-3.6-1.9-6.9h3.8c-.1 3.3-1 5.7-1.9 6.9zm2.6-1.3a15 15 0 0 0 1.3-5.6h3a8 8 0 0 1-4.3 5.6z"/></svg>
        <span>www.company.com</span>
      </li>
      <li>
        <svg viewBox="0 0 24 24" aria-hidden="true"><path d="M12 2a7 7 0 0 0-7 7c0 5.2 7 13 7 13s7-7.8 7-13a7 7 0 0 0-7-7zm0 9.5A2.5 2.5 0 1 1 12 6.5a2.5 2.5 0 0 1 0 5z"/></svg>
        <span>123 Name Street, 000<br>Your City, 00000-000</span>
      </li>
    </ul>
  </div>

  <div class="front-band">
    <span class="band-orange"></span>
    <span class="band-gap"></span>
    <span class="band-black"></span>
  </div>
</section>

<section class="card card-back">
  <div class="concrete-surface" role="img" aria-label="Grey weathered concrete texture background"></div>
  <div class="back-brand">
    <span class="brand-square"></span>
    <span class="brand-name">Quarlwick Builders</span>
  </div>
  <p class="services-line">PATIOS - SIDEWALKS - RETAINING WALLS - FOUNDATIONS</p>
</section>

</body>
</html>
```